Company director needs a business card design

I am a semi-retired former senior finance executive who sits on a number of public and private company boards and do some consulting work. I work largely with emerging businesses but deal regularly with top end of town lawyers, bankers etc. I need a thoughtful but relatively conservative design which would also resonate with my younger client base. Some colour would be good. Information limited to name, address, office tel, mobile and email.

Industry/Entity Type

Finance

```html
<!DOCTYPE html>
<html lang="en">
<head>
<meta charset="utf-8">
<title>Martin Caldwell — Business Card</title>
<link rel="stylesheet" href="https://fonts.googleapis.com/css2?family=Cinzel:wght@400;500&family=Cinzel+Decorative:wght@400&family=Marcellus&display=swap">
<style>
  :root {
    --ink-blue: #0a14c8;
    --accent-orange: #f47b12;
    --paper: #ffffff;
  }
  html, body {
    margin: 0;
    padding: 0;
    width: 1200px;
    height: 661px;
    overflow: hidden;
    background: var(--paper);
  }
  .card {
    position: relative;
    width: 1200px;
    height: 661px;
    box-sizing: border-box;
    border: 5px solid var(--ink-blue);
    background: var(--paper);
  }
  .card-name {
    position: absolute;
    left: 46px;
    top: 40px;
    margin: 0;
    font-family: "Cinzel", serif;
    font-weight: 400;
    font-size: 76px;
    line-height: 1;
    letter-spacing: 2px;
    color: var(--ink-blue);
    white-space: nowrap;
  }
  .card-name .initial {
    font-family: "Cinzel Decorative", serif;
    font-size: 104px;
    color: var(--accent-orange);
    letter-spacing: 0;
  }
  .divider {
    position: absolute;
    left: 598px;
    top: 236px;
    width: 2px;
    height: 393px;
    background: var(--accent-orange);
  }
  .contact {
    position: absolute;
    left: 618px;
    top: 500px;
    margin: 0;
    padding: 0;
    list-style: none;
  }
  .contact-line {
    height: 30px;
    line-height: 30px;
    white-space: nowrap;
  }
  .contact-label {
    font-family: "Cinzel", serif;
    font-size: 26px;
    color: var(--accent-orange);
  }
  .contact-value {
    font-family: "Marcellus", serif;
    font-size: 26px;
    color: var(--ink-blue);
  }
  .contact-value.email {
    font-size: 21px;
  }
  .contact-address {
    margin-top: 6px;
    font-family: "Cinzel", serif;
    font-size: 29px;
    color: var(--ink-blue);
    letter-spacing: 0.5px;
  }
</style>
</head>
<body>
  <div class="card">
    <h1 class="card-name"><span class="initial">M</span>artin <span class="initial">C</span>aldwell</h1>
    <div class="divider"></div>
    <ul class="contact">
      <li class="contact-line"><span class="contact-label">Tel:</span> <span class="contact-value">02 9000 4815</span></li>
      <li class="contact-line"><span class="contact-label">Mobile:</span> <span class="contact-value">0491 570 226</span></li>
      <li class="contact-line"><span class="contact-label">Email:</span> <span class="contact-value email">martin_caldwell@mailpost.net.au</span></li>
      <li class="contact-line contact-address">18 Coral Street, Seaview NSW 2099</li>
    </ul>
  </div>
</body>
</html>
```